Exercise Physiologist needs business cards

I have a logo, I need business cards (Sole trader) as I am moving to a new location and would like an updated look. I provide gym based exercise rehabilitation, injury prevention and movement assessments. I have over 13 years experience as an Exercise Physiologist. I would like the cards to look professional but not boring and can be a little different to stand out when sitting with other Allied Health Professional cards.

Target Market(s)

GP's, Allied health practitioners, people with injuries wanting to exercise

Industry/Entity Type

Health And Wellness

Contact Information for Business Card

Megan Dorrit - Exercise Physiologist 0437 582 906
14 Larkspur Bend Rd
Ellerby Park
(Gate 4, Brannock Fitness)
vantorahealth@maildrop-example.com
socialpage-example.com/Vantora

Requirements
Must have
• I would like to include a section to add next appointment date and time space to the back of the card.
Nice to have
• Rounded corners and a black background on 1 or 2 sides.
Should not have
• Pictures of fit/toned bodies etc

```html
<!DOCTYPE html>
<html lang="en">
<head>
<meta charset="utf-8">
<title>Vantora Health &amp; Rehabilitation – Business Card</title>
<link href="https://fonts.googleapis.com/css2?family=Oswald:wght@300;400;600&display=swap" rel="stylesheet">
<style>
  :root {
    --backdrop: #5b5b5b;
    --card-blue: #5aacdd;
    --card-white: #ffffff;
    --ink-navy: #2457a7;
    --ink-white: #ffffff;
    --pin-blue: #2b62b3;
    --line-grey: #8a94a8;
    --ghost-fill: #f0f3fb;
    --ghost-ring: #e3e7f3;
    --shadow: rgba(0, 0, 0, 0.45);
  }
  * { margin: 0; padding: 0; box-sizing: border-box; }
  html, body {
    width: 1200px;
    height: 1200px;
    overflow: hidden;
    background: var(--backdrop);
    font-family: "Oswald", "Arial Narrow", sans-serif;
  }
  .canvas { position: relative; width: 1200px; height: 1200px; }

  .card {
    position: absolute;
    left: 174px;
    width: 878px;
    height: 502px;
    border-radius: 24px;
    overflow: hidden;
    box-shadow: 8px 8px 8px var(--shadow);
  }
  .card--front { top: 86px; background: var(--card-blue); color: var(--ink-white); }
  .card--back { top: 614px; background: var(--card-white); color: var(--ink-navy); }

  /* brand lockup */
  .brand { position: absolute; display: flex; align-items: center; gap: 16px; z-index: 1; }
  .brand__mark { border-radius: 50%; flex: none; }
  .brand__name { font-weight: 400; line-height: 1.05; white-space: nowrap; }
  .card--front .brand { left: 64px; top: 56px; }
  .card--front .brand__mark { width: 124px; height: 124px; border: 9px solid var(--ink-white); }
  .card--front .brand__name { font-size: 40px; color: var(--ink-white); }
  .card--back .brand { left: 236px; top: 66px; gap: 12px; }
  .card--back .brand__mark { width: 84px; height: 84px; background: var(--card-blue); border: 6px solid var(--ink-navy); }
  .card--back .brand__name { font-size: 28px; color: var(--ink-navy); }

  /* contact block */
  .holder { position: absolute; left: 62px; top: 284px; display: flex; align-items: baseline; gap: 16px; }
  .holder__name { font-weight: 600; font-size: 42px; letter-spacing: 0.5px; }
  .holder__role { font-weight: 300; font-size: 30px; }
  .contact { position: absolute; left: 62px; top: 348px; list-style: none; }
  .contact__item { display: flex; align-items: center; gap: 16px; font-weight: 300; font-size: 30px; height: 48px; white-space: nowrap; }
  .contact__icon { width: 20px; height: 22px; flex: none; }

  /* appointment fields */
  .appointment { position: absolute; left: 95px; top: 270px; z-index: 1; }
  .appointment__row { display: flex; align-items: flex-end; gap: 8px; height: 70px; }
  .appointment__label { font-weight: 400; font-size: 34px; line-height: 1; }
  .appointment__line { width: 308px; border-bottom: 1.5px solid var(--line-grey); margin-bottom: 4px; }

  .ghost-circle { position: absolute; left: 606px; top: 40px; width: 520px; height: 520px;
    border-radius: 50%; background: var(--ghost-fill); border: 22px solid var(--ghost-ring); }
</style>
</head>
<body>
<main class="canvas">

  <section class="card card--front" aria-label="Card front">
    <div class="brand">
      <span class="brand__mark"></span>
      <span class="brand__name">Vantora Health &amp; Rehabilitation</span>
    </div>
    <div class="holder">
      <span class="holder__name">MEGAN DORRIT</span>
      <span class="holder__role">EXERCISE PHYSIOLOGIST</span>
    </div>
    <ul class="contact">
      <li class="contact__item">
        <svg class="contact__icon" viewBox="0 0 20 22" aria-hidden="true">
          <path d="M1 9 Q10 2 19 9 L17 12 L14 10 L14 8 Q10 6.5 6 8 L6 10 L3 12 Z" fill="#2b62b3"/>
          <rect x="4" y="12" width="12" height="7" rx="1.5" fill="#2b62b3"/>
        </svg>
        <span>0437 582 906</span>
      </li>
      <li class="contact__item">
        <svg class="contact__icon" viewBox="0 0 20 22" aria-hidden="true">
          <path d="M10 1 A7.5 7.5 0 0 1 17.5 8.5 C17.5 14 10 21 10 21 C10 21 2.5 14 2.5 8.5 A7.5 7.5 0 0 1 10 1 Z" fill="#2b62b3"/>
          <circle cx="10" cy="8.5" r="3" fill="#5aacdd"/>
        </svg>
        <span>14 Larkspur Bend Rd, Ellerby Park (Gate 4, Brannock Fitness)</span>
      </li>
    </ul>
  </section>

  <section class="card card--back" aria-label="Card back">
    <span class="ghost-circle" aria-hidden="true"></span>
    <div class="brand">
      <span class="brand__mark"></span>
      <span class="brand__name">Vantora Health &amp; Rehabilitation</span>
    </div>
    <div class="appointment">
      <div class="appointment__row">
        <span class="appointment__label">DATE</span>
        <span class="appointment__line"></span>
      </div>
      <div class="appointment__row">
        <span class="appointment__label">TIME</span>
        <span class="appointment__line"></span>
      </div>
    </div>
  </section>

</main>
</body>
</html>
```